Brisk Harbour Finance Business Cards

Looking for a business card for a new mortgage broking business. Name of the business is Brisk Harbour Finance. Purpose of the business is to build trust and strong relationships with clients to then assist them with your mortgage lending needs. Most relationships within the business start off as an enquiry, and then can evolve into a 10+ year relationship, servicing clients from purchasing a new home to then upgrading for their family and even then assisting their children with their first home purchase. Business card should communicate financial security and trust.

Target Market(s)

Targeting professional clients who are looking to build a relationship with a knowledgeable mortgage professional

Industry/Entity Type

Finance - Home Loans

Contact Information for Business Card

Peter Holcroft, Director, mobile: 0471 926058, email:peter@briskharbourfinance.com.au, website: www.briskharbourfinance.com.au

Font styles to use
Sans Serif

Requirements
Must have
• On the front: Must have company logo, contact details as above. On the back: slogan, 'full of choices, free of stress', plus listing services offered: home loans, investment loans, first home buyers, refinancing, car finance

```html
<!DOCTYPE html>
<html lang="en">
<head>
<meta charset="utf-8">
<title>Brisk Harbour Finance – Business Cards</title>
<link href="https://fonts.googleapis.com/css2?family=Montserrat:ital,wght@0,500;0,700;0,800;1,700&family=Lato:wght@400;700&display=swap" rel="stylesheet">
<style>
  :root {
    --navy: #024e78;
    --navy-dark: #013a5a;
    --orange: #f2a20c;
    --white: #ffffff;
    --ink: #1f2a33;
    --stage: #2b2b2b;
  }
  * { box-sizing: border-box; margin: 0; padding: 0; }
  html, body { width: 1200px; height: 875px; overflow: hidden; }
  body {
    background: var(--stage);
    font-family: "Lato", sans-serif;
    display: flex;
    align-items: center;
    justify-content: center;
    gap: 40px;
  }
  .card {
    width: 540px;
    height: 330px;
    border-radius: 18px;
    position: relative;
    display: flex;
    align-items: center;
    overflow: hidden;
  }
  .card--back { background: var(--navy); color: var(--white); }
  .card--front { background: var(--white); color: var(--navy); }

  .brand {
    display: flex;
    align-items: center;
    gap: 14px;
    margin-left: 44px;
    width: 210px;
  }
  .brand__mark {
    width: 16px; height: 16px;
    background: var(--orange);
    flex: none;
  }
  .brand__name {
    font-family: "Montserrat", sans-serif;
    font-weight: 700;
    font-size: 25px;
    line-height: 1.05;
    text-transform: uppercase;
    letter-spacing: 0.5px;
  }
  .card--back .brand__name { color: var(--white); }
  .card--front .brand__name { color: var(--navy); }

  .divider {
    width: 1.5px;
    height: 110px;
    margin: 0 26px 0 10px;
  }
  .card--back .divider { background: rgba(255,255,255,0.55); }
  .card--front .divider { background: var(--navy); }

  .services { list-style: none; }
  .services li {
    display: flex;
    align-items: center;
    gap: 10px;
    font-family: "Lato", sans-serif;
    font-size: 13.5px;
    letter-spacing: 0.6px;
    line-height: 22px;
    text-transform: uppercase;
  }
  .services svg { width: 12px; height: 12px; flex: none; }

  .slogan {
    position: absolute;
    left: 0; right: 0; bottom: 34px;
    text-align: center;
    font-family: "Lato", sans-serif;
    font-size: 17px;
    letter-spacing: 0.4px;
  }
  .slogan strong {
    font-family: "Montserrat", sans-serif;
    font-style: italic;
    font-weight: 700;
  }

  .person__name {
    font-family: "Montserrat", sans-serif;
    font-weight: 800;
    font-size: 22px;
    letter-spacing: 0.8px;
    text-transform: uppercase;
    color: var(--navy);
  }
  .person__role {
    font-size: 14px;
    color: var(--orange);
    margin-bottom: 10px;
  }
  .contacts { list-style: none; }
  .contacts li {
    display: flex;
    align-items: center;
    gap: 9px;
    font-size: 12.5px;
    line-height: 22px;
    color: var(--ink);
  }
  .contacts svg { width: 12px; height: 12px; flex: none; fill: var(--navy); }
</style>
</head>
<body>

  <section class="card card--back" aria-label="Card back">
    <div class="brand">
      <span class="brand__mark"></span>
      <span class="brand__name">Brisk<br>Harbour<br>Finance</span>
    </div>
    <span class="divider"></span>
    <ul class="services">
      <li><svg viewBox="0 0 12 12"><path d="M1 6 6 1.5 11 6M2.5 5v5.5h7V5" fill="none" stroke="var(--orange)" stroke-width="1.4"/></svg>Home Loans</li>
      <li><svg viewBox="0 0 12 12"><path d="M1 6 6 1.5 11 6M2.5 5v5.5h7V5" fill="none" stroke="var(--orange)" stroke-width="1.4"/></svg>Investment Loans</li>
      <li><svg viewBox="0 0 12 12"><path d="M1 6 6 1.5 11 6M2.5 5v5.5h7V5" fill="none" stroke="var(--orange)" stroke-width="1.4"/></svg>First Home Buyers</li>
      <li><svg viewBox="0 0 12 12"><path d="M1 6 6 1.5 11 6M2.5 5v5.5h7V5" fill="none" stroke="var(--orange)" stroke-width="1.4"/></svg>Refinancing</li>
      <li><svg viewBox="0 0 12 12"><path d="M1 6 6 1.5 11 6M2.5 5v5.5h7V5" fill="none" stroke="var(--orange)" stroke-width="1.4"/></svg>Car Finance</li>
    </ul>
    <p class="slogan">Full of <strong>Choices</strong>, Free of <strong>Stress</strong></p>
  </section>

  <section class="card card--front" aria-label="Card front">
    <div class="brand">
      <span class="brand__mark"></span>
      <span class="brand__name">Brisk<br>Harbour<br>Finance</span>
    </div>
    <span class="divider"></span>
    <div class="person">
      <h1 class="person__name">Peter Holcroft</h1>
      <p class="person__role">Director</p>
      <ul class="contacts">
        <li><svg viewBox="0 0 12 12"><path d="M3 1 5 3.5 4 5c.6 1.3 1.7 2.4 3 3l1.5-1L11 9l-1 2C5.5 11 1 6.5 1 2z"/></svg>0471 926058</li>
        <li><svg viewBox="0 0 12 12"><path d="M1 2.5h10v7H1z M1.3 2.8 6 6.5l4.7-3.7" stroke="var(--white)" stroke-width=".8"/></svg>peter@briskharbourfinance.com.au</li>
        <li><svg viewBox="0 0 12 12"><circle cx="6" cy="6" r="5"/><path d="M1 6h10M6 1c-2 2.5-2 7.5 0 10M6 1c2 2.5 2 7.5 0 10" fill="none" stroke="var(--white)" stroke-width=".8"/></svg>www.briskharbourfinance.com.au</li>
      </ul>
    </div>
  </section>

</body>
</html>
```